Lumbra K - Premium Business Cards

Background of Lumbra K
Lumbra Kestrelwood is a cigar mobile lounge where guests become family. A place of luxury, relaxation, and ambiance is the global popularity demand. Lumbra Kestrelwood strives to provide first-class service of quality and products. Our goal is to ensure that every guest is treated and serviced as a VIP.

Lumbra Kestrelwood was founded by Desmond Harkavy Jr in January 2020. After 15 years of cigar reviews and research Desmond decided it was time to launch his own cigar brand and boutique cigar company. With a wealth of knowledge and years of experience Lumbra Kestrelwood was born. With opulence for all cultures, Lumbra Kestrelwood offers hand rolled cigars with premium blend tobacco from sweet to bold imported from Costa Rica, Dominican Republic, and Nicaragua. Thank you for your business!

Objective:
Create a business card template to be used for all employees. Design should communicate premium and classy. And should use earth tone colors.

Design should include:
1. Client wants to incorporate the cigar leaf
2. Logo
3. Tagline: Respect the smoke
3. Content info:
Calvin Mertzlow
Owner
555-617-0384
cmertzlow@lumbrawares.example
lumbrakestrelwood.example

```html
<!DOCTYPE html>
<html lang="en">
<head>
<meta charset="utf-8">
<title>Lumbra K – Business Cards</title>
<link href="https://fonts.googleapis.com/css2?family=Montserrat:wght@700&family=Roboto+Condensed:wght@400;700&display=swap" rel="stylesheet">
<style>
  :root {
    --backdrop: #1c1c1e;
    --leaf-dark: #2e1c10;
    --leaf-mid: #6b4a2c;
    --leaf-light: #8e6a45;
    --card-white: #f7f6f3;
    --ink: #161616;
    --rule-grey: #9a9a9a;
    --paper-text: #ffffff;
  }
  * { margin: 0; padding: 0; box-sizing: border-box; }
  html, body { width: 1200px; height: 874px; overflow: hidden; background: var(--backdrop); }
  .canvas { position: relative; width: 1200px; height: 874px; }
  .card {
    position: absolute; left: 280px; width: 640px; height: 366px;
    border-radius: 18px; overflow: hidden;
  }
  .card-front { top: 54px; }
  .card-back { top: 454px; background: var(--card-white); }

  .leaf-photo {
    position: absolute; inset: 0;
    background:
      radial-gradient(ellipse at 55% 45%, var(--leaf-light) 0%, transparent 55%),
      radial-gradient(ellipse at 20% 80%, var(--leaf-mid) 0%, transparent 50%),
      linear-gradient(135deg, var(--leaf-dark), var(--leaf-mid) 50%, var(--leaf-dark));
  }

  .brand { position: absolute; text-align: center; }
  .brand-name {
    font-family: "Montserrat", sans-serif; font-weight: 700;
    letter-spacing: 2px; white-space: nowrap;
  }
  .brand-tagline {
    display: flex; align-items: center; justify-content: center; gap: 10px;
    font-family: "Roboto Condensed", sans-serif; font-weight: 700;
    text-transform: uppercase; letter-spacing: 2px; margin-top: 4px;
  }
  .brand-tagline::before, .brand-tagline::after {
    content: ""; flex: 1; height: 1px; background: currentColor; opacity: .7;
  }

  .card-front .brand { left: 0; right: 0; top: 136px; padding: 0 60px; color: var(--paper-text); }
  .card-front .brand-name { font-size: 38px; }
  .card-front .brand-tagline { font-size: 16px; }

  .card-back .brand { left: 40px; top: 60px; width: 340px; color: var(--ink); }
  .card-back .brand-name { font-size: 28px; letter-spacing: 1px; }
  .card-back .brand-tagline { font-size: 12px; color: #555; }

  .person { position: absolute; left: 40px; top: 188px; color: var(--ink); font-family: "Roboto Condensed", sans-serif; }
  .person-name { font-weight: 700; font-size: 24px; letter-spacing: .5px; text-transform: uppercase; }
  .person-role { font-size: 14px; margin-top: 2px; }

  .swoosh { position: absolute; inset: 0; }
  .contact {
    position: absolute; right: 30px; bottom: 24px; list-style: none;
    font-family: "Roboto Condensed", sans-serif; font-size: 17px; color: var(--paper-text);
    text-align: right; line-height: 24px;
  }
  .contact li { display: flex; justify-content: flex-end; align-items: center; gap: 10px; }
  .contact .web { font-weight: 700; }
  .contact svg { width: 14px; height: 14px; flex: none; }
  .icon-fill { fill: var(--paper-text); }
  .icon-line { fill: none; stroke: var(--paper-text); stroke-width: 2; }
</style>
</head>
<body>
<main class="canvas">
  <section class="card card-front">
    <div class="leaf-photo" role="img" aria-label="Close-up photograph of dried cigar tobacco leaves"></div>
    <div class="brand">
      <div class="brand-name">LUMBRA KESTRELWOOD</div>
      <div class="brand-tagline">Respect the smoke</div>
    </div>
  </section>

  <section class="card card-back">
    <svg class="swoosh" viewBox="0 0 640 366" preserveAspectRatio="none" aria-hidden="true">
      <path d="M20,350 C220,268 430,178 640,132" fill="none" stroke="var(--rule-grey)" stroke-width="3"/>
      <path d="M0,366 L0,356 C210,300 420,204 640,152 L640,366 Z" fill="var(--ink)"/>
    </svg>
    <div class="brand">
      <div class="brand-name">LUMBRA KESTRELWOOD</div>
      <div class="brand-tagline">Respect the smoke</div>
    </div>
    <div class="person">
      <div class="person-name">Calvin Mertzlow</div>
      <div class="person-role">Owner</div>
    </div>
    <ul class="contact">
      <li>555-617-0384
        <svg viewBox="0 0 24 24" aria-hidden="true"><path class="icon-fill" d="M6.6 10.8a15 15 0 0 0 6.6 6.6l2.2-2.2a1 1 0 0 1 1-.25 11.4 11.4 0 0 0 3.6.57 1 1 0 0 1 1 1V20a1 1 0 0 1-1 1A17 17 0 0 1 3 4a1 1 0 0 1 1-1h3.5a1 1 0 0 1 1 1c0 1.25.2 2.45.57 3.57a1 1 0 0 1-.25 1z"/></svg>
      </li>
      <li>cmertzlow@lumbrawares.example
        <svg viewBox="0 0 24 24" aria-hidden="true"><path class="icon-line" d="M2 5h20v14H2z M2 5l10 8 10-8"/></svg>
      </li>
      <li class="web">lumbrakestrelwood.example
        <svg viewBox="0 0 24 24" aria-hidden="true">
          <circle class="icon-line" cx="12" cy="12" r="10"/>
          <ellipse class="icon-line" cx="12" cy="12" rx="4.5" ry="10"/>
          <path class="icon-line" d="M2 12h20M4 7h16M4 17h16"/>
        </svg>
      </li>
    </ul>
  </section>
</main>
</body>
</html>
```